2 x storefront vinyl request

We are transitioning to a storefront office and need two vinyls for the windows.

First vinyl: Use the Aldwick Partners logo, website (www.aldwickpartnersestates.example) and leasing office number ((555) 318-4726)

Second vinyl: Maintenance Division & phone number (555) 318-4726

```html
<!DOCTYPE html>
<html lang="en">
<head>
<meta charset="utf-8">
<title>Aldwick Partners – Storefront Vinyls</title>
<link rel="stylesheet" href="https://fonts.googleapis.com/css2?family=Roboto+Condensed:wght@500;700&display=swap">
<style>
  :root {
    --backdrop: #737373;
    --ink: #2b2a29;
    --panel-light: #f4f4f4;
    --panel-mid: #d9d9d9;
    --panel-shade: #c4c4c4;
    --band: #2b2a29;
    --band-text: #ffffff;
  }
  * { margin: 0; padding: 0; box-sizing: border-box; }
  html, body { width: 1200px; height: 515px; overflow: hidden; }
  body {
    background: var(--backdrop);
    font-family: "Roboto Condensed", "Arial Narrow", sans-serif;
    color: var(--ink);
    position: relative;
  }
  .vinyl {
    position: absolute;
    top: 41px;
    width: 537px;
    height: 429px;
    overflow: hidden;
  }
  .vinyl--brand {
    left: 40px;
    background:
      radial-gradient(ellipse 70% 55% at 85% 20%, rgba(255,255,255,0.9), transparent 70%),
      linear-gradient(160deg, var(--panel-mid) 0%, var(--panel-light) 45%, var(--panel-mid) 75%, var(--panel-light) 100%);
  }
  .vinyl--maintenance {
    left: 621px;
  }
  .scene-fill {
    position: absolute;
    inset: 0;
    background:
      radial-gradient(ellipse 80% 60% at 50% 10%, rgba(255,255,255,0.85), transparent 70%),
      linear-gradient(180deg, #e6e6e6 0%, #c9c9c9 45%, #bdbdbd 70%, #d6d6d6 100%);
  }
  .brand-name {
    position: absolute;
    left: 131px;
    top: 115px;
    font-weight: 700;
    font-size: 31px;
    line-height: 30px;
    text-transform: uppercase;
  }
  .brand-name span { display: block; }
  .brand-name span:nth-child(2) { padding-left: 27px; }
  .brand-name span:nth-child(3) { padding-left: 42px; }
  .phone {
    position: absolute;
    display: flex;
    align-items: center;
    font-weight: 700;
    white-space: nowrap;
  }
  .phone svg { flex: none; }
  .vinyl--brand .phone {
    left: 66px;
    top: 304px;
    font-size: 52px;
    gap: 12px;
  }
  .vinyl--brand .phone svg { width: 46px; height: 46px; }
  .web-band {
    position: absolute;
    left: 0; right: 0; bottom: 0;
    height: 59px;
    background: var(--band);
    color: var(--band-text);
    display: flex;
    align-items: center;
    gap: 9px;
    padding-left: 29px;
    font-weight: 500;
    font-size: 33px;
  }
  .web-band svg { width: 30px; height: 30px; flex: none; }
  .division-title {
    position: absolute;
    left: 0; right: 0;
    top: 106px;
    text-align: center;
    font-weight: 700;
    font-size: 74px;
    line-height: 93px;
    letter-spacing: 1px;
    text-transform: uppercase;
  }
  .vinyl--maintenance .phone {
    left: 55px;
    top: 328px;
    font-size: 55px;
    gap: 14px;
  }
  .vinyl--maintenance .phone svg { width: 48px; height: 48px; }
</style>
</head>
<body>
  <svg width="0" height="0" style="position:absolute">
    <defs>
      <symbol id="icon-phone" viewBox="0 0 48 48">
        <path fill="currentColor" d="M10 4c2-1 4 0 5 2l4 8c1 2 0 4-1 5l-3 3c2 5 6 9 11 11l3-3c1-1 3-2 5-1l8 4c2 1 3 3 2 5l-2 5c-1 2-3 3-5 3C19 46 2 29 2 11c0-2 1-4 3-5z"/>
        <path fill="none" stroke="currentColor" stroke-width="2.4" stroke-linecap="round" d="M29 12a8 8 0 0 1 7 7M30 6a14 14 0 0 1 12 12M28 17a3 3 0 0 1 3 3"/>
      </symbol>
      <symbol id="icon-globe" viewBox="0 0 32 32">
        <g fill="none" stroke="currentColor" stroke-width="2.4">
          <circle cx="16" cy="16" r="14"/>
          <ellipse cx="16" cy="16" rx="6" ry="14"/>
          <path d="M2 16h28M4.5 9h23M4.5 23h23M16 2v28"/>
        </g>
      </symbol>
    </defs>
  </svg>

  <section class="vinyl vinyl--brand">
    <h1 class="brand-name"><span>Aldwick</span><span>Partners</span><span>Properties</span></h1>
    <p class="phone"><svg><use href="#icon-phone"/></svg>(555) 318-4726</p>
    <p class="web-band"><svg><use href="#icon-globe"/></svg>aldwickpartnersestates.example</p>
  </section>

  <section class="vinyl vinyl--maintenance">
    <div class="scene-fill" role="img" aria-label="Faded photograph of a large suburban house with a paved front walkway"></div>
    <h2 class="division-title">Maintenance<br>Division</h2>
    <p class="phone"><svg><use href="#icon-phone"/></svg>(555) 318-4726</p>
  </section>
</body>
</html>
```